Wordpress Design Project

WHO WE ARE:
Bright Path Media Group is not just another SEO or PPC company. We work with our clients to help them grow their business and achieve their goals. Our commitment to doing what is best for the customer, is why we have grown so quickly. We believe our business is not about advertising BUT about connecting customers & growing our clients businesses. We see our product as helping people, not selling a product.

PROJECT OVERVIEW:
I need to create a wordpress website for my business, www.brightpathmediagroup.com.au

I need a whole new site created showing all of my services. The services include:
NOTE: These are not the main focus of the home page.

Consulting & Strategy Planning
Search Engine Optimisation
Pay Per Click
Re-Marketing

Once I have selected the top home page design, I will need a product and blog page designed.

SITE DESIGN:
If I was to explain the kind of style I am looking for, it would be high-street, New York agency look, web 2.0. Clean, elegant, stylish, high quality and simple looking. Kind of like you would expect from an plumtree website.

Think of car advertising, the closest to the target market & look/feel Im looking for would be Ferrandell, Korva, Mirel, Talvance, Brisk.

However, I am open to any design style.

DO NOT let this restrict your creativity BUT here are some websites I like the look of.

Home page:
http://www.layoutharbor.example/demo/52816.html
https://www.quorvix.example/intl/en/vantel/devices/
http://www.quorvix.example/intl/en/vantel/devices/features-different.html
http://www.layoutharbor.example/demo/63924.html
https://www.quorvix.example/intl/en/vantel/browser/features.html

Product Page:
http://www.quorvix.example/intl/en/vantel/devices/buynow.html#instore

NOTE: I just added a file called "I like this color scheme.png" you can play around with something like this as well.

Please do not use the content from my current website. That is for a PPC service, the new site is for an full service agency.

Also, the message/tagline is the feature or most prominent element of the website..... Not the services we offer, these are secondary.

Great designs so far everyone, but I think I'm looking a little simpler and less crowded.  Closer to the sample sites I sent.... keep em coming.

Also, I would prefer that the 4 services, do not visually over power the tag line.  The 4 services are not important to the home page.

Lets make this easy, since every design I receive is almost the same...

Make the design look something like these 2 websites.
https://www.quorvix.example/intl/en/vantel/browser/features.html#simplicity

Target Market(s)

Business Owners and entreprenuers who are well established, typically in the 35-60 year old range and spend 100k-1m in advertising per year. They big brands that target these people are Ferrandell, Korva, Mirel, Talvance, Brisk, this should give you the feel for what I am after.

Industry/Entity Type

Advertising

Requirements
Must have
• 1. Navigations: Home, Services, About Us, Blog, Contact Us

2. The main home page words should be.... "We Grow Your Business Online" and "Clear Aim, Clear Plan, Clear Team, Bright Path Media Group" (should use logo for last one)
I would like to see this tagline somewhere in the site "We Don't Want to be the Biggest, Just the Best!"

3. Product page must have a contact form with (name, email, phone, website)
This form must show an offer of "Free Strategy Sessions, Double your website leads", I have included an image to show as an example for the lead form "lead form example.png", see attached.

Nice to have
• I would like to see 1 or 2 of these idea's in the design.

1. I have attached some logos for Promiq & Metrisq certifications + Web association logo you can use for design purposes.

2. You can put company logo's in the design and I can change them to my clients logos at a later date.

3. Testimonials

4. Since our business is about people, pictures of people like business owners, customers using technology such as an slato, or anything like that would be good. However, is not necessary. Some idea: http://www.netmeshly.example/advertising
Should not have
• There will be no video on the design.

```html
<!DOCTYPE html>
<html lang="en">
<head>
<meta charset="utf-8">
<title>Bright Path Media Group</title>
<link href="https://fonts.googleapis.com/css2?family=Arimo:ital,wght@0,400;0,700;1,400&family=Gelasio&display=swap" rel="stylesheet">
<style>
:root{
  --ink:#222;
  --text:#555;
  --muted:#777;
  --blue:#1c63b7;
  --blue-dark:#16509a;
  --green:#5a9a0a;
  --line:#d9d9d9;
  --band:#dcdcdc;
  --footer:#2a2927;
  --footer-text:#6f6e6b;
  --footer-head:#c9c9c9;
  --icon:#8a8a8a;
}
*{margin:0;padding:0;box-sizing:border-box}
html,body{width:1200px;height:1069px;overflow:hidden;background:#fff}
body{position:relative;font-family:"Arimo",Arial,sans-serif;color:var(--text)}
.abs{position:absolute}

/* header */
.site-header{position:absolute;left:0;top:0;width:1200px;height:76px;background:#fff;border-top:3px solid #2b2b2b;box-shadow:0 2px 6px rgba(0,0,0,.18);z-index:2}
.account-tab{position:absolute;left:809px;top:-3px;width:85px;height:18px;background:#3a3a3a;border-radius:0 0 3px 3px;font-size:9px;color:#bbb;display:flex;justify-content:space-around;align-items:center}
.brand{position:absolute;left:306px;top:17px;display:flex;align-items:center;gap:9px}
.brand-mark{width:34px;height:34px;border-radius:50%;background:var(--blue)}
.brand-name{font-size:14px;line-height:14px;font-weight:700;color:#333;letter-spacing:-.2px}
.main-nav{position:absolute;left:483px;top:31px;display:flex;font-size:9.5px;color:#222}
.main-nav a{color:inherit;text-decoration:none;margin-right:24px}
.main-nav a.is-active{color:var(--blue)}

/* hero */
.hero-visual{left:606px;top:110px;width:252px;height:180px;background:linear-gradient(90deg,#fff 0,#fff 18%,#e4e6ea 45%,#c9ced5 75%,#eceef0 100%)}
.hero-title{left:331px;top:123px;font-size:34px;line-height:31px;color:#333;font-weight:400;letter-spacing:-.6px;z-index:1}
.hero-title .accent{color:var(--green)}
.hero-title .line2{display:block;margin-left:59px}
.hero-sub{left:333px;top:197px;font-size:10.4px;letter-spacing:-.15px;color:#555;z-index:1;white-space:nowrap}
.hero-button{left:446px;top:241px;width:116px;height:30px;background:linear-gradient(#2c74c8,var(--blue-dark));color:#fff;font-size:12px;display:flex;align-items:center;padding-left:9px;box-shadow:0 6px 8px -4px rgba(0,0,0,.35);z-index:1}
.hero-button .play{position:absolute;right:0;top:0;width:36px;height:30px;border-left:1px solid #144a8d;display:flex;align-items:center;justify-content:center}
.slider-arrow{top:186px}
.slider-dots{left:577px;top:304px;display:flex;gap:6px}
.slider-dots span{width:10px;height:10px;border-radius:50%;background:#c4c4c4}
.slider-dots span.is-current{background:var(--blue)}

/* services */
.service-card{width:288px;height:114px;background:#fff;border:1px solid #ddd}
.service-card::after{content:"";position:absolute;left:6px;right:6px;bottom:-10px;height:10px;background:radial-gradient(ellipse at top,rgba(0,0,0,.22),rgba(0,0,0,0) 70%)}
.service-card h2{position:absolute;left:67px;top:5px;font-size:15px;font-weight:400;color:#222}
.service-card p{position:absolute;left:68px;top:30px;width:206px;font-size:8.4px;line-height:13px;color:#888}
.service-card svg{position:absolute;left:5px;top:30px}

/* testimonials */
.section-title{left:306px;top:652px;font-size:11px;font-weight:700;color:#222}
.section-rule{left:427px;top:648px;width:473px;height:21px;background:var(--band)}
.testimonial{top:696px;width:180px;text-align:center}
.testimonial blockquote{font-size:8.6px;line-height:13px;font-style:italic;color:#666}
.testimonial cite{display:block;font-style:normal;font-size:8.6px;color:#222;font-weight:700;margin-top:12px}
.testimonial cite span{font-weight:400;color:#5a78a8}
.motto{left:0;top:817px;width:1200px;text-align:center;font-family:"Gelasio",Georgia,serif;font-size:18px;color:#7a7a7a}

/* footer */
.footer-band{left:0;top:866px;width:1200px;height:20px;background:var(--band)}
.site-footer{position:absolute;left:0;top:886px;width:1200px;height:183px;background:var(--footer)}
.footer-rule{left:306px;top:26px;width:584px;height:1px;background:#4a4946}
.footer-head{top:10px;font-size:10px;font-weight:400;color:var(--footer-head)}
.footer-list{top:48px;font-size:7px;line-height:9.5px;color:var(--footer-text)}
.footer-list li{list-style:none}
.footer-list .gap{margin-top:9px}
.footer-links li{margin-bottom:9.5px}
.field{width:129px;height:22px;background:#fff;font-size:7px;color:#333;padding:7px 4px}
.submit{left:845px;top:109px;width:42px;height:14px;background:var(--blue);color:#fff;font-size:9px;text-align:center;line-height:14px}
.social{top:149px;display:flex;gap:10px}
.social span{width:14px;height:14px;background:#55544f}
.copyright{right:313px;top:159px;font-size:8px;color:#55544f}
</style>
</head>
<body>

<header class="site-header">
  <div class="account-tab"><span>Login</span><span>Register</span></div>
  <div class="brand"><span class="brand-mark"></span><span class="brand-name">Bright Path<br>Media Group</span></div>
  <nav class="main-nav">
    <a class="is-active" href="#">HOME</a>
    <a href="#">SERVICES</a>
    <a href="#">ABOUT US</a>
    <a href="#">BLOG</a>
    <a href="#">CONTACT US</a>
  </nav>
</header>

<section class="hero">
  <svg class="abs slider-arrow" style="left:270px" width="18" height="32" viewBox="0 0 18 32"><polyline points="15,1 2,16 15,31" fill="none" stroke="#888" stroke-width="1.2"/></svg>
  <svg class="abs slider-arrow" style="left:885px" width="18" height="32" viewBox="0 0 18 32"><polyline points="3,1 16,16 3,31" fill="none" stroke="#888" stroke-width="1.2"/></svg>

  <div class="abs hero-visual" role="img" aria-label="Laptop showing a dart hitting the centre of a target"></div>
  <h1 class="abs hero-title">We <span class="accent">Grow</span> Your<span class="line2">Business Online</span></h1>
  <p class="abs hero-sub">Clear Aim, Clear Plan, Clear Team, Bright Path Media Group</p>
  <a class="abs hero-button">Learn NOW!
    <span class="play"><svg width="16" height="16" viewBox="0 0 16 16"><circle cx="8" cy="8" r="7.5" fill="#3a7fcf"/><polygon points="6,4.5 11.5,8 6,11.5" fill="#174f95"/></svg></span>
  </a>
  <div class="abs slider-dots"><span></span><span class="is-current"></span><span></span></div>
</section>

<section class="services">
  <article class="abs service-card" style="left:306px;top:348px">
    <svg width="56" height="54" viewBox="0 0 56 54"><ellipse cx="40" cy="12" rx="12" ry="9" fill="var(--icon)"/><polygon points="33,19 30,27 38,20" fill="var(--icon)"/><circle cx="22" cy="22" r="8" fill="var(--icon)"/><path d="M5 52 Q6 32 22 32 Q38 32 38 52 Z" fill="var(--icon)"/></svg>
    <h2>Consulting &amp; Strategy Planning</h2>
    <p>Lorem ipsum dolor sit amet, consetetur sadipscing elitr, sed diam nonumy eirmod tempor invidunt ut labore et dolore magna aliquyam erat, sed diam voluptua. At vero eos et accusam et justo duo dolores et ea rebum.</p>
  </article>
  <article class="abs service-card" style="left:606px;top:348px">
    <svg width="56" height="54" viewBox="0 0 56 54"><circle cx="22" cy="22" r="13" fill="none" stroke="var(--icon)" stroke-width="5"/><line x1="31" y1="32" x2="45" y2="47" stroke="var(--icon)" stroke-width="7" stroke-linecap="round"/></svg>
    <h2>Search Engine Optimisation</h2>
    <p>Consetetur sadipscing elitr, sed diam nonumy eirmod tempor invidunt ut labore et dolore magna aliquyam erat, sed diam voluptua. At vero eos et accusam et justo duo dolores et ea rebum.</p>
  </article>
  <article class="abs service-card" style="left:306px;top:494px">
    <svg width="56" height="54" viewBox="0 0 56 54"><path d="M8 6 L28 6 L52 30 L32 50 L8 26 Z" fill="var(--icon)"/><circle cx="16" cy="14" r="3" fill="#fff"/><text x="30" y="35" font-size="16" font-weight="700" fill="#fff" text-anchor="middle" font-family="Arimo,sans-serif" transform="rotate(45 30 30)">$</text></svg>
    <h2>Pay Per Click</h2>
    <p>No sea takimata sanctus est Lorem ipsum dolor sit amet. Lorem ipsum dolor sit amet, consetetur sadipscing elitr, sed diam nonumy eirmod tempor invidunt ut labor At vero eos et accusam et justo duo dolores et ea rebum.</p>
  </article>
  <article class="abs service-card" style="left:606px;top:494px">
    <svg width="60" height="54" viewBox="0 0 60 54"><circle cx="14" cy="20" r="6" fill="var(--icon)"/><path d="M3 42 Q3 28 14 28 Q25 28 25 42 Z" fill="var(--icon)"/><circle cx="46" cy="20" r="6" fill="var(--icon)"/><path d="M35 42 Q35 28 46 28 Q57 28 57 42 Z" fill="var(--icon)"/><circle cx="30" cy="17" r="7" fill="var(--icon)"/><path d="M17 42 Q17 26 30 26 Q43 26 43 42 Z" fill="var(--icon)"/></svg>
    <h2>Re-Marketing</h2>
    <p>Stet clita kasd gubergren, no sea takimata sanctus est Lorem ipsum dolor sit amet. Lorem ipsum dolor sit amet, consetetur sadipscing elitr, sed diam nonumy eirmod tempor .</p>
  </article>
</section>

<section class="testimonials">
  <h3 class="abs section-title">WHAT PEOPLE SAY?</h3>
  <div class="abs section-rule"></div>
  <figure class="abs testimonial" style="left:307px">
    <blockquote>Ut wisi enim ad minim veniam, quis nostrud exerci tation ullamcorper suscipit lobortis nisl ut aliquip ex ea commodo consequat. Duis autem vel eum iriure dolor in hendrerit in vulputate velit esse molestie consequat.</blockquote>
    <cite>Ellis Varner - <span>Manager Director</span></cite>
  </figure>
  <figure class="abs testimonial" style="left:514px;top:695px">
    <blockquote>vel illum dolore eu feugiat nulla facilisis at vero eros et accumsan et iusto odio dignissim qui blandit praesent luptatum zzril delenit augue duis dolore te feugait.</blockquote>
    <cite>Nadia Corlow - <span>Manager Director</span></cite>
  </figure>
  <figure class="abs testimonial" style="left:713px;top:695px">
    <blockquote>Nam liber tempor cum soluta nobis eleifend option congue nihil imperdiet doming id quod mazim placerat facer possim assum. Lorem ipsum dolor sit amet, consectetuer adipiscing elit.</blockquote>
    <cite>Tobin Haskell - <span>Manager Director</span></cite>
  </figure>
  <p class="abs motto">"We Don't Want to be the Biggest, Just the Best!"</p>
</section>

<div class="abs footer-band"></div>
<footer class="site-footer">
  <div class="abs footer-rule"></div>
  <h4 class="abs footer-head" style="left:310px">CONTACT</h4>
  <h4 class="abs footer-head" style="left:492px">OUR SERVICES</h4>
  <h4 class="abs footer-head" style="left:641px">LINK</h4>
  <h4 class="abs footer-head" style="left:757px">NEWSLETTER</h4>

  <ul class="abs footer-list" style="left:312px">
    <li>Phone &nbsp;&nbsp;&nbsp;&nbsp;&nbsp;&nbsp;: &nbsp;+61 2 5550 1042</li>
    <li>Fax &nbsp;&nbsp;&nbsp;&nbsp;&nbsp;&nbsp;&nbsp;&nbsp;&nbsp;&nbsp;: &nbsp;+61 2 5550 1043</li>
    <li class="gap">Mail &nbsp;&nbsp;&nbsp;&nbsp;&nbsp;&nbsp;&nbsp;&nbsp;: &nbsp;PO Box 118 LINDEN VALE 2790</li>
    <li>Email &nbsp;&nbsp;&nbsp;&nbsp;&nbsp;&nbsp;&nbsp;: &nbsp;sales@brightpath.example</li>
    <li class="gap">ABN 00 000 000 000</li>
    <li>7-9 Linden Road (PO Box 118)</li>
    <li>LINDEN VALE 2790 Australia</li>
  </ul>
  <ul class="abs footer-list footer-links" style="left:493px">
    <li>Duis autem vel eum iriure dolor</li>
    <li>In hendrerit in vulputate velit</li>
    <li>Esse molestie consequat,</li>
    <li>Vel illum dolore eu feugiat</li>
    <li>At vero eos et accusam</li>
  </ul>
  <ul class="abs footer-list footer-links" style="left:641px">
    <li>Home</li>
    <li>About Us</li>
    <li>Products</li>
    <li>Contact Us</li>
  </ul>

  <div class="abs field" style="left:758px;top:49px">Username</div>
  <div class="abs field" style="left:758px;top:79px">Email</div>
  <div class="abs submit">Submit</div>

  <div class="abs social" style="left:313px"><span></span><span></span><span></span></div>
  <p class="abs copyright">All rights reserved. Bright Path Media Group, Copyright © 2012</p>
</footer>

</body>
</html>
```